Minimalist Modern Business Card Design, open to ideas, or cleaner version of provided files, but what logo & logo colors (with some black) as shown in files, and info for back shown in files as well.

```html
<!DOCTYPE html>
<html lang="en">
<head>
<meta charset="utf-8">
<title>Roadside Rig Works – Business Card</title>
<link href="https://fonts.googleapis.com/css2?family=Montserrat:wght@600&family=Open+Sans:wght@400;700&display=swap" rel="stylesheet">
<style>
  :root {
    --navy: #2e2a78;
    --ink: #1a1a1a;
    --paper: #ffffff;
    --backdrop: #232323;
  }
  * { margin: 0; padding: 0; box-sizing: border-box; }
  html, body { width: 1200px; height: 711px; overflow: hidden; background: var(--backdrop); }
  body { position: relative; font-family: "Open Sans", sans-serif; color: var(--ink); }

  .card {
    position: absolute;
    left: 341px;
    width: 519px;
    height: 296px;
    background: var(--paper);
    overflow: hidden;
  }
  .card--front { top: 45px; }
  .card--back { top: 370px; }

  .brand { position: absolute; display: flex; align-items: center; gap: 12px; }
  .brand__mark { background: var(--navy); flex: none; }
  .brand__name {
    font-family: "Montserrat", sans-serif;
    font-weight: 600;
    color: var(--navy);
    line-height: 0.98;
  }
  .card--front .brand { left: 159px; top: 17px; }
  .card--front .brand__mark { width: 30px; height: 30px; }
  .card--front .brand__name { font-size: 23px; }
  .card--back .brand { left: 19px; top: 20px; gap: 16px; }
  .card--back .brand__mark { width: 36px; height: 36px; }
  .card--back .brand__name { font-size: 27px; }

  .list-block { position: absolute; top: 69px; }
  .list-block--services { left: 18px; }
  .list-block--specialties { left: 361px; }
  .list-block__title { font-weight: 700; font-size: 13px; letter-spacing: 0.2px; line-height: 16px; margin-bottom: 2px; }
  .list-block__items { list-style: none; }
  .list-block__items li {
    position: relative;
    padding-left: 14px;
    font-size: 11.6px;
    line-height: 15.9px;
  }
  .list-block--specialties .list-block__items li { padding-left: 16px; }
  .list-block__items li::before {
    content: "";
    position: absolute;
    left: 1px; top: 5px;
    width: 5.5px; height: 5.5px;
    background: var(--navy);
    transform: rotate(45deg);
  }

  .region-band {
    position: absolute;
    left: 0; top: 259px;
    width: 100%; height: 19px;
    background: var(--navy);
    color: var(--paper);
    font-size: 12.5px;
  }
  .region-band span { position: absolute; top: 0; line-height: 19px; transform: translateX(-50%); }
  .region-band .sep {
    top: 7px; width: 5.5px; height: 5.5px;
    background: var(--paper);
    transform: translateX(-50%) rotate(45deg);
  }

  .person { position: absolute; right: 23px; top: 126px; text-align: right; }
  .person__name { font-size: 25px; font-weight: 700; color: var(--navy); line-height: 28px; letter-spacing: 0.3px; }
  .person__title { font-size: 15.5px; font-weight: 700; line-height: 18px; }
  .accent-bar { position: absolute; right: 0; top: 125px; width: 15px; height: 47px; background: var(--navy); }

  .contact { position: absolute; left: 19px; top: 237px; font-size: 14.5px; line-height: 19px; }
  .contact__row { display: flex; }
  .contact__label { width: 21px; font-weight: 700; color: var(--navy); font-size: 16px; }
</style>
</head>
<body>

  <section class="card card--front">
    <div class="brand">
      <span class="brand__mark"></span>
      <div class="brand__name">Roadside<br>Rig Works</div>
    </div>

    <div class="list-block list-block--services">
      <h2 class="list-block__title">SERVICES INCLUDE:</h2>
      <ul class="list-block__items">
        <li>Shop &amp; Mobile</li>
        <li>DOT &amp; BIT Inspections</li>
        <li>All Maintenance &amp; Repairs</li>
        <li>Check Engine Lights</li>
        <li>Diags, Regens &amp; Programming</li>
        <li>Full Dealer Software Capabilities</li>
        <li>PM &amp; Compliance Tracking</li>
        <li>App-Based Billing &amp; Live Updates</li>
        <li>Dealer Certified Techs</li>
        <li>Night Servicing to Avoid Downtime</li>
      </ul>
    </div>

    <div class="list-block list-block--specialties">
      <h2 class="list-block__title">SPECIALIZING IN:</h2>
      <ul class="list-block__items">
        <li>Heavy &amp; Medium Duty</li>
        <li>Corvane</li>
        <li>Izaro</li>
        <li>Hevro</li>
        <li>Pettaline</li>
        <li>Freightmark</li>
        <li>Kestrel Haul</li>
        <li>Alliver</li>
        <li>After Treatment</li>
        <li>And More</li>
      </ul>
    </div>

    <div class="region-band">
      <span style="left:39px">LA</span>
      <span class="sep" style="left:149px"></span>
      <span style="left:259px">OC</span>
      <span class="sep" style="left:369px"></span>
      <span style="left:479px">IE</span>
    </div>
  </section>

  <section class="card card--back">
    <div class="brand">
      <span class="brand__mark"></span>
      <div class="brand__name">Roadside<br>Rig Works</div>
    </div>

    <div class="person">
      <div class="person__name">MY NAME</div>
      <div class="person__title">President</div>
    </div>
    <span class="accent-bar"></span>

    <div class="contact">
      <div class="contact__row"><span class="contact__label">M</span><span>123-123-4567</span></div>
      <div class="contact__row"><span class="contact__label">E</span><span>xxxxxxx@xxxxxx.com</span></div>
    </div>
  </section>

</body>
</html>
```